I need a business card design for a new dance business. I offer classical Indian dance tuition and also professional performances. I want to offer the community a variety of Indian dance experiences which include: group class and private tuition, school and preschool educational courses and workshops. dance theatre performances, community function workshops and performances, Kids Bollywood parties, wedding & conference performances, mouth percussion classes, Indian mythology/ dance costume and make up workshops.
The final design should communicate a feeling and impression of the vibrance and energy of Indian dance.
Updates
Hi Everyone,
Project Deadline Extended
Reason: I would like to refine a few changes to the details of this lovely design and we have run out of time!
Project Deadline Extended
Reason: Still waiting to hear back form designer re two possible changes to the card design. Tomorrow is the deadline and I have sent several messages but with no response. I need to see this through before selecting this lovely design.
Thank you.
Tara
Industry/Entity Type
Preschool
Requirements
Must have
- The front of the business card should have the photo of me (my face and torso), surrounded entirely by a border of bright magenta (to match the magenta of my lipstick - it is the same as the magenta on my skirt in the second photo). Within the top border I want (perhaps yellow-gold) writing to say "Tara Holloway - Artistic Director" and within the bottom border it should read "Silver Creek Kathak Studio." If you turn the card on its side the left border should have my telephone number: 0417 826 394 and the right-hand border should read: silvercreekkathakstudio@fernmail.example
The reverse of the card should be the orange of the dance costume
and I'd like the picture of my feet and legs to be on the right side of the back of the card as a side border. Centre-aligned on the orange background it should read (perhaps in dark magenta):
Indian dance classes + private tuition
School + preschool educational courses and workshops
Dance theatre performances
Community function workshops and performances
Children's Bollywood parties
Wedding + conference performances
Mouth percussion classes
Indian mythology and dance demonstration workshops
Dance costume and make-up workshops
Nice to have
- A lovely artistic but easy-to-read font would be nice.

```html
<!DOCTYPE html>
<html lang="en">
<head>
<meta charset="utf-8">
<title>Tara Holloway – Silver Creek Kathak Studio</title>
<link rel="stylesheet" href="https://fonts.googleapis.com/css2?family=Yatra+One&family=Source+Sans+3:wght@300;400&display=swap">
<style>
  :root {
    --magenta: #e0228b;
    --gold: #f4c430;
    --saffron: #eaa41f;
    --plum: #7a1f4a;
    --backdrop: #d8d6d0;
    --skin: #e2b9a4;
    --hair: #2b1a17;
    --sari-orange: #f0a21c;
    --sari-maroon: #7a1838;
    --pearl: #f1e6e0;
  }
  * { margin: 0; padding: 0; box-sizing: border-box; }
  html, body {
    width: 1200px; height: 899px; overflow: hidden; background: #ffffff;
  }
  .card {
    position: relative; width: 1200px; height: 899px; overflow: hidden;
    display: grid; grid-template-columns: 372px 659px 169px;
  }

  /* Portrait area */
  .portrait {
    position: relative;
    background:
      radial-gradient(ellipse 150px 110px at 150px 60px, var(--hair) 0%, rgba(43,26,23,0.85) 55%, rgba(43,26,23,0) 100%),
      radial-gradient(ellipse 150px 200px at 150px 250px, var(--skin) 0%, rgba(226,185,164,0.9) 60%, rgba(226,185,164,0) 100%),
      radial-gradient(ellipse 120px 330px at 170px 720px, var(--sari-maroon) 0%, rgba(122,24,56,0.9) 55%, rgba(122,24,56,0) 100%),
      linear-gradient(180deg, var(--backdrop) 0%, var(--backdrop) 45%, var(--sari-orange) 58%, var(--sari-orange) 100%);
  }

  /* Central magenta panel */
  .title-panel {
    position: relative; background: var(--magenta);
    font-family: "Yatra One", cursive; text-align: center;
  }
  .name {
    position: absolute; top: 90px; left: 0; right: 0;
    color: var(--gold); font-size: 66px; font-weight: 400; line-height: 1;
    display: flex; align-items: center; justify-content: center; gap: 28px;
  }
  .diamond {
    width: 13px; height: 13px; background: var(--gold); transform: rotate(45deg);
  }
  .role {
    position: absolute; top: 180px; left: 0; right: 0;
    color: var(--gold); font-size: 46px; line-height: 1;
  }
  .dancer {
    position: absolute; border-radius: 50% 50% 18% 18% / 30% 30% 14% 14%;
  }
  .dancer-side { top: 391px; width: 126px; height: 191px; background: var(--plum); }
  .dancer-left { left: 94px; }
  .dancer-right { left: 428px; }
  .dancer-centre { top: 313px; left: 235px; width: 176px; height: 269px; background: var(--saffron); }
  .studio {
    position: absolute; left: 0; right: 0; color: var(--plum); line-height: 1;
  }
  .studio-top { top: 692px; font-size: 50px; }
  .studio-bottom { top: 760px; font-size: 64px; }

  /* Contact strip */
  .contact-strip {
    position: relative; background: var(--saffron);
    font-family: "Source Sans 3", sans-serif; font-weight: 300; color: var(--plum);
  }
  .contact {
    position: absolute; top: 50%; left: 50%; white-space: nowrap;
    transform-origin: center; line-height: 1;
  }
  .phone { font-size: 46px; letter-spacing: 0.04em; transform: translate(-50%, -50%) translate(-36px, -5px) rotate(-90deg); }
  .email { font-size: 41px; transform: translate(-50%, -50%) translate(28px, 6px) rotate(-90deg); }
</style>
</head>
<body>
  <main class="card">
    <div class="portrait" role="img" aria-label="Photograph of the artistic director in classical dance costume, flower hair ornaments, jewellery and an orange and maroon sari"></div>
    <section class="title-panel">
      <h1 class="name"><span class="diamond"></span>Tara Holloway<span class="diamond"></span></h1>
      <p class="role">artistic director</p>
      <div class="dancer dancer-side dancer-left" role="img" aria-label="Illustration of a seated dancer in meditation pose"></div>
      <div class="dancer dancer-centre" role="img" aria-label="Illustration of a central seated dancer with raised arms"></div>
      <div class="dancer dancer-side dancer-right" role="img" aria-label="Illustration of a seated dancer in meditation pose"></div>
      <p class="studio studio-top">Silver Creek</p>
      <p class="studio studio-bottom">Kathak Studio</p>
    </section>
    <aside class="contact-strip">
      <p class="contact phone">0417 826 394</p>
      <p class="contact email">silvercreekkathakstudio@fernmail.example</p>
    </aside>
  </main>
</body>
</html>
```